International Property Consultancy

Brief Overview:

I need a dynamic and well designed website that is easy to use and understand. It has to be unique and different to generic templates that most websites seem to be these days. PLEASE NO GENERIC TEMPLATES FROM THE INTERNET.

Our business has 10 years experience working on struggling international developments that we then work in-house for to turn around and brings bout success. We stay within a project often for long periods of time until success is achieved. We are unique in our approach and completely different to the standard routes to market for many developments. The site is for developers to see what we have done in regards to previous projects, as such we want to incorporate video into this site with a strong design aesthetic. There will be videos of the past projects we have worked on, which will act as case studies.

I like very simple but punchy websites, that people can navigate and understand very easily. Also a big fan of unique and well thought out design aesthetic.

Initial Site layout thoughts:

1) Homepage:
2) About Us
3) What we've done / Work
This part has the projects we have worked on (France, Portugal, London, Morocco). Each one will have some video content and photo images, but also would be good to have a succinct way to mention what we did and the successes in a clever and punchy way.

4) Contact Us

* This is just a guideline. Would be open to input and creative direction on your own part.

*More details and websites we like can be seen in the brief doc attached.

PLEASE VIEW THE WIREFRAME WORD DOC ATTACHED.

Here there are also some more examples to help:

Here are just a few examples of websites and what I like about them:

- www.velmoro.com (clean, nice geometric design aesthetic, good animation when loading and changing pages well thought out all though also coulee be considered a bit dull and basic after the initial homepage slide)
- https://www.farbridgehub.net (Clean site, quite clinical, lacks video content and doesn't engage greatly).
- https://ruskotile.com (minimal, and like how it mixes the design aesthetic more with video and photo content)

- https://www.amberquillworks.com (like the layout of this and how it displays the projects and work section)

- https://brisk.com (Good use of video content)

- https://loomfield.studio (minimal to the point and mixes design with video and animation etc...)

Here is another couple of cool websites that may help give you some direction: https://halvenquay.com www.brisk.com

Hi there, One of the things I thought would be good on the homepage is to add the logo with a 'digital landscape' before flicking down into a slide with video content of the projects... Just an idea but have posted some pics in the brief. We would get this animated for the site. But if you have better ideas, please do run with them. Thanks,

Target Market(s)

Property developers

Number of Pages Required

4 page

Font styles to use
Other font styles liked:
• Read brief

Requirements
Must have
• Needs to be clean, dynamic and easy to follow on desktop and mobile. We will use it as a kind of portfolio website so will need to embed video of past projects we have worked on.

Read brief in docs.
Nice to have
• Clean
Should not have
• Not be another generic template website.
Not have random property stock photos. (We are not a property agency).

```html
<!DOCTYPE html>
<html lang="en">
<head>
<meta charset="utf-8">
<title>Calvessa — International Property Developments</title>
<link rel="stylesheet" href="https://fonts.googleapis.com/css2?family=Red+Hat+Display:wght@400;500;700&display=swap">
<style>
:root{
  --ink:#1c1f26;
  --text:#2a2a2a;
  --muted:#555;
  --line:#333;
  --white:#fff;
  --footer:#1f1f1f;
  --footer-text:#d8d8d8;
  --teal:#1f4e5f;
  --green:#6a9a2c;
  --pink:#d0166e;
  --blue:#4b3fe0;
  --yellow:#f2c230;
  --magenta:#e54fd6;
  --social:#3b5bb8;
}
*{box-sizing:border-box;margin:0;padding:0}
html,body{width:1200px;height:2943px;overflow:hidden}
body{position:relative;background:var(--white);font-family:"Red Hat Display",sans-serif;color:var(--text)}
.abs{position:absolute}
.header{left:0;top:0;width:1200px;height:96px;background:var(--white)}
.brand{left:94px;top:24px;font-size:44px;font-weight:500;color:var(--ink);letter-spacing:-0.5px}
.menu-toggle{left:1074px;top:42px;width:32px;height:14px}
.menu-toggle span{position:absolute;right:0;height:2px;background:var(--ink)}
.hero{left:0;top:96px;width:1200px;height:560px;background:linear-gradient(180deg,#e4e4e4 0%,#ececec 55%,#fafafa 92%,#fff 100%)}
.hero-title{left:0;top:305px;width:1200px;text-align:center;font-size:50px;font-weight:700;color:var(--ink)}
.hero-sub{left:0;top:362px;width:1200px;text-align:center;font-size:38px;font-weight:400;color:var(--ink)}
.accent{position:absolute}
.photo{position:absolute;box-shadow:0 8px 18px rgba(0,0,0,.18)}
.rule{position:absolute;height:2px;background:var(--line)}
.rule-short{position:absolute;height:1px;width:40px;background:#777}
.heading{position:absolute;font-size:19px;font-weight:500;color:var(--ink);line-height:1.2}
.copy{position:absolute;font-size:13.5px;line-height:21px;color:var(--text)}
.btn{position:absolute;height:40px;border:1.5px solid var(--ink);background:var(--white);font-size:15px;font-weight:700;color:var(--ink);display:flex;align-items:center;justify-content:center}
.btn::after{content:"";position:absolute;right:-20px;top:19px;width:30px;height:1.5px;background:var(--ink)}
.about-bg{left:0;top:1040px;width:1200px;height:560px;background:linear-gradient(180deg,#fff 0%,#ececec 20%,#e6e6e6 75%,#fff 100%)}
.play{position:absolute;left:654px;top:1240px;width:64px;height:64px}
.card-label{position:absolute;font-size:20px;color:var(--white)}
.gallery-tile{position:absolute;top:2385px;width:240px;height:212px}
.footer{left:0;top:2597px;width:1200px;height:346px;background:var(--footer)}
.foot-head{position:absolute;top:2652px;font-size:15px;font-weight:700;color:var(--white)}
.foot-rule{position:absolute;top:2691px;width:34px;height:1px;background:#aaa}
.foot-link{position:absolute;font-size:12.5px;color:var(--footer-text)}
.email-field{left:821px;top:2686px;width:285px;height:36px;background:var(--white);font-size:11px;color:#777;padding:0 15px;display:flex;align-items:center}
.submit{left:821px;top:2734px;width:120px;height:36px;background:var(--white);font-size:14px;font-weight:700;color:var(--ink);display:flex;align-items:center;justify-content:center}
.social{position:absolute;top:2797px;width:26px;height:26px;border-radius:50%}
.copyright{left:0;top:2870px;width:1200px;text-align:center;font-size:12px;color:var(--footer-text)}
</style>
</head>
<body>

<header class="abs header">
  <div class="abs brand">calvessa.</div>
  <div class="abs menu-toggle"><span style="top:0;width:32px"></span><span style="top:8px;width:22px"></span></div>
</header>

<section class="abs hero" role="img" aria-label="Faded greyscale photo of a modern house interior with a staircase"></section>
<span class="accent" style="left:93px;top:206px;width:8px;height:40px;background:var(--teal)"></span>
<span class="accent" style="left:398px;top:206px;width:9px;height:43px;background:var(--green)"></span>
<span class="accent" style="left:800px;top:147px;width:21px;height:5px;background:var(--pink)"></span>
<span class="accent" style="left:1028px;top:160px;width:8px;height:43px;background:var(--blue)"></span>
<span class="accent" style="left:1017px;top:455px;width:9px;height:40px;background:var(--yellow)"></span>
<span class="accent" style="left:397px;top:559px;width:36px;height:6px;background:var(--magenta)"></span>
<h1 class="abs hero-title">We are Calvessa</h1>
<p class="abs hero-sub">We fulfill international property developments</p>

<!-- Delivered projects -->
<div class="photo" style="left:96px;top:603px;width:491px;height:282px;background:linear-gradient(180deg,#5d6f94 0%,#2a2c33 45%,#2b3a1e 100%)" role="img" aria-label="Modern black two-storey house at dusk with lit windows"></div>
<div class="photo" style="left:448px;top:738px;width:341px;height:281px;background:linear-gradient(180deg,#7c8da8 0%,#3b3530 50%,#2f4a1f 100%)" role="img" aria-label="Contemporary house with a large tree and lit interior at dusk"></div>
<div class="rule" style="left:674px;top:741px;width:128px"></div>
<h2 class="heading" style="left:837px;top:730px">The projects we have delivered</h2>
<div class="rule-short" style="left:840px;top:768px"></div>
<p class="copy" style="left:838px;top:786px;width:280px">We deliver a unique and truly bespoke approach to delivering international developments to market, with over 10 years success around the world.</p>
<div class="btn" style="left:839px;top:894px;width:140px">See Our Work</div>

<!-- About -->
<div class="abs about-bg" role="img" aria-label="Faded greyscale photo of a street with modern houses"></div>
<h2 class="heading" style="left:97px;top:1170px">About Calvessa</h2>
<div class="rule" style="left:320px;top:1180px;width:128px"></div>
<div class="rule-short" style="left:98px;top:1208px"></div>
<p class="copy" style="left:96px;top:1226px;width:350px">We fulfil international property developments in a truly unique way. We've worked on projects around the world taking developments from fields to award winning resorts, and tired underachieving developments to overachieving goliaths.</p>
<div class="btn" style="left:94px;top:1357px;width:140px">Know More</div>
<div class="photo" style="left:795px;top:1177px;width:403px;height:385px;background:linear-gradient(180deg,#7b8aa0 0%,#2b2b2e 45%,#44502c 80%,#5a5a55 100%)" role="img" aria-label="Black modern house with wooden accents and lawn at dusk"></div>
<div class="photo" style="left:504px;top:1106px;width:366px;height:359px;border:2px solid var(--white);background:linear-gradient(180deg,#3f6aa8 0%,#9fb2c6 35%,#8a8074 65%,#6e6358 100%)" role="img" aria-label="Video still of a modern house with a slatted fence"></div>
<svg class="play" viewBox="0 0 64 64" aria-hidden="true">
  <path d="M32 4 A28 28 0 1 1 8 46" fill="none" stroke="#fff" stroke-width="3"/>
  <path d="M25 20 L46 32 L25 44 Z" fill="#fff"/>
</svg>

<!-- Work -->
<div class="photo" style="left:0;top:1655px;width:94px;height:249px;background:linear-gradient(180deg,#5a4434 0%,#b8a58c 60%,#9c8a6c 100%)" role="img" aria-label="Interior with wooden staircase"></div>
<div class="card-label" style="left:-8px;top:1768px;font-size:28px;color:rgba(255,255,255,.75)">ance</div>
<div class="photo" style="left:102px;top:1655px;width:218px;height:249px;background:linear-gradient(180deg,#3a3836 0%,#4d4a46 55%,#3a2a20 100%)" role="img" aria-label="Interior dining space with dark wood floor"></div>
<div class="card-label" style="left:102px;top:1766px;width:218px;text-align:center;font-size:28px;color:rgba(255,255,255,.55)">London</div>
<div class="photo" style="left:330px;top:1621px;width:450px;height:316px;background:linear-gradient(180deg,#1f2f78 0%,#28336a 35%,#4a3a2c 70%,#101010 100%)" role="img" aria-label="Symmetrical resort buildings around a pool at night"></div>
<div class="card-label" style="left:330px;top:1893px;width:450px;text-align:center">Portugal Resort</div>
<div class="rule" style="left:734px;top:1685px;width:75px"></div>
<h2 class="heading" style="left:838px;top:1674px;width:230px">We did and the success of the project</h2>
<div class="rule-short" style="left:840px;top:1735px"></div>
<p class="copy" style="left:836px;top:1752px;width:280px">By creating a unique and bespoke in-house white-label strategy that allows each project to be the only beneficiary of the work we do.</p>
<div class="btn" style="left:834px;top:1840px;width:140px">See Our Work</div>

<!-- News -->
<div class="abs" style="left:0;top:1960px;width:1200px;height:425px;background:linear-gradient(180deg,#fff 0%,#f1f1f1 60%,#e8e8e8 100%)" role="img" aria-label="Faded greyscale photo of a house facade"></div>
<div class="photo" style="left:93px;top:2009px;width:406px;height:304px;background:linear-gradient(180deg,#c7ccd2 0%,#e9e9e6 45%,#b9b7b1 100%)" role="img" aria-label="White modern villa with palm trees"></div>
<div class="rule" style="left:473px;top:2042px;width:64px"></div>
<h2 class="heading" style="left:558px;top:2032px">Our Recent News<br>&amp; Blog</h2>
<div class="btn" style="left:950px;top:2030px;width:139px">View More</div>
<p class="copy" style="left:557px;top:2107px;width:500px">By creating a unique and bespoke in-house white-label strategy that allows each project to be the only beneficiary of the work we do.</p>
<div class="photo" style="left:401px;top:2183px;width:225px;height:130px;background:linear-gradient(180deg,#3c4a3a 0%,#8e8d86 60%,#6b6b66 100%)" role="img" aria-label="White villa with dark trees"></div>
<div class="photo" style="left:641px;top:2183px;width:225px;height:130px;background:linear-gradient(180deg,#9fc0dd 0%,#e6dcc6 50%,#86a84a 100%)" role="img" aria-label="Single-storey house with green lawn"></div>
<div class="photo" style="left:880px;top:2183px;width:225px;height:130px;background:linear-gradient(180deg,#5f86b8 0%,#c9a98a 50%,#6f9a40 100%)" role="img" aria-label="Brick house with garage and lawn"></div>

<!-- Gallery -->
<div class="gallery-tile" style="left:0;background:linear-gradient(180deg,#5d86b6 0%,#6a5a3a 55%,#6d6d68 100%)" role="img" aria-label="Bungalow with lit windows at evening"></div>
<div class="gallery-tile" style="left:240px;background:linear-gradient(180deg,#3c4250 0%,#6b6a66 50%,#2f3138 100%)" role="img" aria-label="Modern house with balcony by the water"></div>
<div class="gallery-tile" style="left:480px;background:linear-gradient(180deg,#2d3a4a 0%,#2c3a26 55%,#3e6a22 100%)" role="img" aria-label="Large house behind a green lawn"></div>
<svg class="abs" style="left:582px;top:2472px" width="36" height="36" viewBox="0 0 36 36" aria-hidden="true"><circle cx="18" cy="18" r="16" fill="none" stroke="#fff" stroke-width="3"/></svg>
<div class="gallery-tile" style="left:720px;background:linear-gradient(180deg,#8fb4d8 0%,#8a7058 50%,#a19a8c 100%)" role="img" aria-label="Stone cottage with driveway"></div>
<div class="gallery-tile" style="left:960px;background:linear-gradient(135deg,#3e7bc2 0%,#5b8fce 45%,#e8d6b6 55%,#cdb894 100%)" role="img" aria-label="Pale house gable against blue sky"></div>

<!-- Footer -->
<footer class="abs footer"></footer>
<div class="foot-head" style="left:96px">Quick Link</div>
<div class="foot-rule" style="left:99px"></div>
<div class="foot-link" style="left:99px;top:2714px">Home</div>
<div class="foot-link" style="left:99px;top:2745px">About</div>
<div class="foot-link" style="left:99px;top:2776px">Work</div>
<div class="foot-link" style="left:99px;top:2807px">Contact Us</div>

<div class="foot-head" style="left:310px">Our Work</div>
<div class="foot-rule" style="left:311px"></div>
<div class="foot-link" style="left:312px;top:2714px">Portugal Resort</div>
<div class="foot-link" style="left:312px;top:2745px">Morocco</div>
<div class="foot-link" style="left:312px;top:2776px">London</div>
<div class="foot-link" style="left:312px;top:2807px">France</div>

<div class="foot-head" style="left:537px">Contact Us</div>
<div class="foot-rule" style="left:540px"></div>
<div class="foot-link" style="left:541px;top:2714px;line-height:20px">320 W Lorem Ipsum<br>Lorem.12 Ipsum.</div>
<div class="foot-link" style="left:541px;top:2766px">hello@calvessa.com</div>
<div class="foot-link" style="left:541px;top:2796px">+0 123 456 789</div>

<div class="foot-head" style="left:819px">Contact Us</div>
<div class="abs email-field">Enter Email id:</div>
<div class="abs submit">Submit Now</div>
<span class="social" style="left:819px;background:var(--social)"></span>
<span class="social" style="left:851px;background:var(--social)"></span>
<span class="social" style="left:883px;background:var(--social)"></span>
<span class="social" style="left:916px;background:var(--social)"></span>
<div class="abs copyright">Copyright © 2020 Calvessa. All rights reserved.</div>

</body>
</html>
```